Pediatric Pelvic Health Brochure

Looking to design a brochure for Marlow Brook's pelvic health program. I can provide imagery once I see the layout. Our website is marlowbrookpt.example so the look should reflect that

If you see PDF titled blue and word doc you will see what we provided as thoguhts.

Target Market(s)

parents of children

Industry/Entity Type

Health And Wellness

Font styles to use
Serif

Requirements
Must have
• clear call outs - easy to read with copy,
Should not have
• not look bland or dated

```html
<!DOCTYPE html>
<html lang="en">
<head>
<meta charset="utf-8">
<title>Pediatric Pelvic Health – Marlow Brook's</title>
<link rel="stylesheet" href="https://fonts.googleapis.com/css2?family=Bebas+Neue&family=Tinos&display=swap">
<style>
  :root {
    --page-bg: #e9edf2;
    --blue-light: #5bbcf0;
    --blue-mid: #4a8fcc;
    --blue-deep: #2f5f98;
    --blue-slate: #5b87b5;
    --band-dark: #3f6fa3;
    --white: #ffffff;
    --text-soft: #dfe6ee;
    --text-muted: #d2dbe6;
    --icon-cyan: #1fa6d6;
    --photo-grey: #c9cfd6;
    --photo-warm: #e2d6cc;
    --photo-sky: #a9cfe2;
  }
  html, body {
    margin: 0;
    padding: 0;
    overflow: hidden;
    background: var(--page-bg);
  }
  .brochure {
    position: relative;
    width: 1200px;
    height: 848px;
    overflow: hidden;
    font-family: "Tinos", "Times New Roman", serif;
  }
  .brochure__art {
    position: absolute;
    inset: 0;
  }
  .section-heading {
    position: absolute;
    margin: 0;
    font-family: "Bebas Neue", sans-serif;
    font-weight: 400;
    font-size: 33px;
    letter-spacing: 0.5px;
    line-height: 1;
    padding: 6px 6px 4px;
    background: linear-gradient(90deg, rgba(255,255,255,0) 0%, rgba(255,255,255,0.08) 100%);
  }
  .section-heading::after {
    content: "";
    position: absolute;
    left: 18px;
    right: 40px;
    bottom: -10px;
    height: 4px;
    border-radius: 50%;
    background: rgba(20, 45, 80, 0.45);
    filter: blur(2px);
  }
  .specialize__heading {
    left: 96px;
    top: 418px;
    color: var(--white);
  }
  .contact__heading {
    left: 497px;
    top: 424px;
    color: var(--text-soft);
  }
  .specialize__body {
    position: absolute;
    left: 47px;
    top: 487px;
    width: 285px;
    margin: 0;
    color: var(--white);
    font-size: 16.3px;
    line-height: 23px;
    text-align: justify;
    word-spacing: 3px;
  }
  .specialize__body p { margin: 0 0 23px; }
  .specialize__body p:last-child { margin: 0; }
  .specialize__rule {
    position: absolute;
    left: 50px;
    top: 821px;
    width: 160px;
    height: 4px;
    border-radius: 50%;
    background: rgba(20, 45, 80, 0.45);
    filter: blur(2px);
  }
  .contact__intro {
    position: absolute;
    left: 453px;
    top: 498px;
    width: 220px;
    margin: 0;
    color: var(--text-muted);
    font-size: 16.3px;
    line-height: 24.3px;
    word-spacing: 4px;
  }
  .contact__list {
    position: absolute;
    left: 458px;
    top: 628px;
    margin: 0;
    padding: 0;
    list-style: none;
    color: var(--text-soft);
    font-size: 16.3px;
    line-height: 24.3px;
    word-spacing: 4px;
  }
  .contact__item {
    position: absolute;
    left: 0;
    display: flex;
    align-items: flex-start;
    white-space: nowrap;
  }
  .contact__item svg {
    width: 38px;
    height: 38px;
    flex: none;
  }
  .contact__item span { margin-left: 75px; }
  .contact__item--phone { top: 0; }
  .contact__item--phone span { margin-top: 8px; }
  .contact__item--address { top: 50px; }
  .contact__item--address span { margin-top: -2px; }
  .contact__item--web { top: 134px; }
  .contact__item--web span { margin-top: 10px; }
  .cover__title {
    position: absolute;
    left: 792px;
    width: 408px;
    top: 585px;
    margin: 0;
    text-align: center;
    color: var(--text-soft);
    font-weight: 400;
    font-size: 44px;
    line-height: 56px;
    letter-spacing: 1px;
    word-spacing: 8px;
  }
  .cover__tagline {
    position: absolute;
    left: 792px;
    width: 408px;
    top: 708px;
    margin: 0;
    text-align: center;
    color: var(--text-soft);
    font-size: 19px;
    line-height: 28.5px;
    word-spacing: 5px;
  }
</style>
</head>
<body>
<main class="brochure">
  <svg class="brochure__art" width="1200" height="848" viewBox="0 0 1200 848" aria-hidden="false">
    <defs>
      <linearGradient id="panel-left" x1="0" y1="0" x2="0" y2="1">
        <stop offset="0" stop-color="var(--blue-light)"/>
        <stop offset="0.55" stop-color="var(--blue-mid)"/>
        <stop offset="1" stop-color="var(--blue-deep)"/>
      </linearGradient>
      <linearGradient id="panel-middle" x1="0" y1="0" x2="1" y2="1">
        <stop offset="0" stop-color="#58a8dc"/>
        <stop offset="0.6" stop-color="#4d7fb6"/>
        <stop offset="1" stop-color="#6c96c4"/>
      </linearGradient>
      <linearGradient id="panel-right" x1="0" y1="0" x2="0" y2="1">
        <stop offset="0" stop-color="#6aa0cf"/>
        <stop offset="1" stop-color="var(--blue-slate)"/>
      </linearGradient>
      <linearGradient id="photo-left" x1="0" y1="0" x2="1" y2="1">
        <stop offset="0" stop-color="var(--photo-grey)"/>
        <stop offset="1" stop-color="var(--photo-warm)"/>
      </linearGradient>
      <linearGradient id="photo-middle" x1="0" y1="0" x2="1" y2="1">
        <stop offset="0" stop-color="#b9bec6"/>
        <stop offset="1" stop-color="#e6e8ec"/>
      </linearGradient>
      <linearGradient id="photo-right" x1="0" y1="0" x2="1" y2="1">
        <stop offset="0" stop-color="var(--photo-sky)"/>
        <stop offset="1" stop-color="#eef2f5"/>
      </linearGradient>
      <clipPath id="photo-area">
        <path d="M0,0 L0,204 C80,270 160,305 230,303 C290,300 330,285 366,266 C420,230 500,160 546,112 C600,220 700,360 792,418 L800,423 C860,440 930,452 993,449 C1080,440 1150,390 1200,334 L1200,0 Z"/>
      </clipPath>
      <filter id="band-shadow" x="-5%" y="-20%" width="110%" height="140%">
        <feDropShadow dx="0" dy="3" stdDeviation="2.5" flood-color="#1c3556" flood-opacity="0.55"/>
      </filter>
    </defs>

    <rect class="panel panel--left" x="0" y="0" width="366" height="848" fill="url(#panel-left)"/>
    <rect class="panel panel--middle" x="366" y="0" width="426" height="848" fill="url(#panel-middle)"/>
    <rect class="panel panel--right" x="792" y="0" width="408" height="848" fill="url(#panel-right)"/>

    <path class="wave-band" d="M0,204 C80,270 160,305 230,303 C290,300 330,285 366,266 C420,230 500,160 546,112 C600,220 700,360 792,418 C860,440 930,452 993,449 C1080,440 1150,390 1200,334 L1200,420 C1120,480 1010,560 900,545 C760,515 640,330 546,210 C470,310 380,395 260,402 C180,407 90,360 0,262 Z" fill="var(--band-dark)" opacity="0.85"/>

    <g clip-path="url(#photo-area)">
      <rect x="0" y="0" width="366" height="320" fill="url(#photo-left)" role="img" aria-label="Photo: smiling patient talking with a clinician"/>
      <rect x="366" y="0" width="426" height="430" fill="url(#photo-middle)" role="img" aria-label="Photo: caring therapist in a white coat"/>
      <rect x="792" y="0" width="408" height="460" fill="url(#photo-right)" role="img" aria-label="Photo: friendly physical therapy team in a bright clinic"/>
    </g>

    <path class="wave-line" d="M0,262 C90,360 180,407 260,402 C380,395 470,310 546,210 C640,330 760,515 900,545 C1010,560 1120,480 1200,420" fill="none" stroke="var(--white)" stroke-width="20" filter="url(#band-shadow)"/>
  </svg>

  <section class="specialize">
    <h2 class="section-heading specialize__heading">We Specialize</h2>
    <div class="specialize__body">
      <p>All pelvic physical therapy treatments are always done with a physical therapist trained in pediatric pelvic floor issues, and always with your doctor’s knowledge. Children are dressed and parents and guardians are present.</p>
      <p>During each session, your child or teen will work exclusively with one of our pelvic health physical therapists to help build strength, improve movement, and strengthen the skills</p>
    </div>
    <div class="specialize__rule"></div>
  </section>

  <section class="contact">
    <h2 class="section-heading contact__heading">Contact Us</h2>
    <p class="contact__intro">We offer a FREE 15 minute consultation to help you determine if therapy is right for you.</p>
    <ul class="contact__list">
      <li class="contact__item contact__item--phone">
        <svg viewBox="0 0 38 38" fill="none" stroke="var(--icon-cyan)" stroke-width="1.6" stroke-linejoin="round">
          <rect x="14" y="3" width="21" height="15" rx="1"/>
          <path d="M14 3 L24.5 12 L35 3"/>
          <path d="M4 14 C2 18 5 27 13 33 C16 35 19 35 20 33 L21 31 L16 27 L13.5 29 C10 26 8 22 7.5 19 L10 17 L7 11 Z"/>
        </svg>
        <span>212.555.0148</span>
      </li>
      <li class="contact__item contact__item--address">
        <svg viewBox="0 0 38 38" fill="none" stroke="var(--icon-cyan)" stroke-width="2.4" stroke-linejoin="round">
          <path d="M19 29 C11 20 6 16 6 12 A13 11 0 0 1 32 12 C32 16 27 20 19 29 Z"/>
          <ellipse cx="19" cy="12" rx="7" ry="5"/>
          <path d="M8 29 L4 36 L34 36 L30 29"/>
        </svg>
        <span>418 Linden Avenue<br>Ground Floor<br>New York, NY 10021</span>
      </li>
      <li class="contact__item contact__item--web">
        <svg viewBox="0 0 38 38" fill="none" stroke="var(--icon-cyan)" stroke-width="2.2">
          <circle cx="19" cy="19" r="16"/>
          <ellipse cx="19" cy="19" rx="7" ry="16"/>
          <path d="M3 19 H35 M6 11 H32 M6 27 H32 M19 3 V35"/>
        </svg>
        <span>marlowbrookpt.example</span>
      </li>
    </ul>
  </section>

  <section class="cover">
    <h1 class="cover__title">PEDIATRIC<br>PELVIC HEALTH</h1>
    <p class="cover__tagline">Treating Infants, Children<br>&amp; Adolescents</p>
  </section>
</main>
</body>
</html>
```